High-End Medical Center Website Design Project

This design is part of a well thought-out project by an experienced project manager / developer. The approved wireframe is attached. Creative interpretations / suggestions based on the layout encouraged.

The design is for a new state-of-the-art medical center located in Dallas, Texas. The target audience would likely be individuals (approx. 60% female /40% male) who are the healthcare decision-makers for their families. They would likely have insurance and be inclined to seek out top-quality care.

Potential clients would choose this client over others in their industry because the medical center is physician owned, meaning it is patient-focused rather than profit-focused. The facility is brand new, featuring the latest technology. (This includes an amazing waiting room featuring WiFi and docking stations.) The physicians are hand-picked by referral only.

The look of the site should be extremely clean. We are going for a well-organized, professional look with a bit of a warm glow (interpret that however you like). Use crisp corners and the colors in the logo.

Think modern, clean with some great use of color / font.

We can get lovely photography of the medical center once construction is complete. Feel free to use an "example image" behind the Featured Area ("Physician Owned. Patient-Focused") if you like. We are open to ideas.

ONE CHANGE REQUESTED IN THE WIREFRAME:

Remove the "Connect" 1/4 page footer area and replace with a quick contact form. You may swap the "Locations" area with the form if desired. Put social media icons at the top left of the page in the top header area.

(Note: Please use social media icons that match the design rather than standard icons. We preferred not placing the icons at the top, but the client requested this. Let's not bring more attention to them than necessary.)
Updates

We're custom programming this site, so there's no need to base it on a template. Also, we would prefer not to use typical "seen everywhere" stock images.Thanks.

Industry/Entity Type

Construction

Requirements
Must have
• Follow the wireframe. This has been approved.
Nice to have
• Examples of what hover states, links or dropdowns might look like.

```html
<!DOCTYPE html>
<html lang="en">
<head>
<meta charset="utf-8">
<title>Crest Medical Center</title>
<link href="https://fonts.googleapis.com/css2?family=Open+Sans:ital,wght@0,300;0,400;0,600;0,700;1,400;1,600&display=swap" rel="stylesheet">
<style>
:root{
  --blue:#0a58a8;
  --blue-dark:#084c92;
  --teal:#45adb9;
  --teal-deep:#3a9fad;
  --teal-light:#6fd3e0;
  --ink:#555;
  --grey-bg:#f2f2f2;
  --white:#fff;
}
*{margin:0;padding:0;box-sizing:border-box}
html,body{width:1056px;height:1200px;overflow:hidden}
body{font-family:'Open Sans',sans-serif;background:var(--white);position:relative;color:var(--ink)}
.abs{position:absolute}
/* top bar */
.topbar{left:0;top:0;width:1056px;height:26px;background:var(--blue)}
.social{left:190px;top:6px;display:flex;gap:6px}
.social span{width:14px;height:14px;border:1px solid rgba(255,255,255,.7)}
.social span:first-child{background:var(--teal);border-color:var(--teal)}
.call{right:190px;top:6px;color:var(--white);font-size:10px}
/* header */
.brand{left:190px;top:44px;height:29px;display:flex;align-items:center;gap:8px}
.brand i{width:16px;height:16px;background:var(--blue);display:block}
.brand b{font-size:20px;font-weight:700;color:var(--blue);letter-spacing:.5px}
.nav{right:190px;top:54px;display:flex;font-size:10px;color:#666}
.nav a{padding:0 9px;border-left:1px solid #ccc;line-height:12px;text-decoration:none;color:inherit}
.nav a:first-child{border:0}
.nav a.active{color:var(--blue);border-left:2px solid var(--blue);padding-left:10px;height:40px;margin-top:0}
.nav a.last{padding-right:0}
.nav small{display:block;font-size:7px;color:#999;margin-top:2px}
.dropdown{left:731px;top:93px;width:135px;height:77px;background:var(--blue);padding-top:6px;font-size:10px;color:var(--white)}
.dropdown div{height:21px;line-height:21px;padding-left:14px}
.dropdown .hover{background:var(--teal)}
/* hero */
.hero{left:0;top:93px;width:1056px;height:461px;background:linear-gradient(110deg,#d9d6d0 0%,#b9b2a8 35%,#8c96ad 65%,#c9bfae 100%)}
.headline{left:276px;top:241px;width:504px;height:43px;background:var(--blue);color:var(--white);font-size:23px;font-weight:700;text-align:center;line-height:43px;letter-spacing:.3px}
.subline{left:276px;top:293px;width:504px;text-align:center;color:var(--white);font-size:12.5px;font-style:italic;font-weight:600;line-height:18px;text-shadow:0 1px 2px rgba(0,0,0,.3)}
.dots{left:501px;top:341px;display:flex;gap:7px}
.dots span{width:5px;height:5px;border-radius:50%;background:var(--white)}
.diamond{top:400px;width:59px;height:59px;transform:rotate(45deg)}
.diamond svg{transform:rotate(-45deg);width:59px;height:59px}
/* features */
.feat-img{left:190px;top:581px;width:184px;height:110px;background:linear-gradient(135deg,#7da3c4,#4f7fa8 60%,#9ab6cc)}
.feat-img p{position:absolute;left:0;right:0;top:40px;text-align:center;color:var(--white);font-size:16px;font-weight:300;line-height:19px}
.feat-img p b{font-weight:700;font-size:20px}
.feat{top:581px;height:110px;color:#d6ecf6;font-size:9.2px;text-align:center;line-height:12.8px;padding:8px 18px 0}
.feat h3{font-size:10px;font-weight:600;color:var(--white);margin-bottom:9px;position:relative}
.feat.teal{background:var(--teal);color:var(--white)}
.feat.blue{background:var(--blue)}
/* about band */
.band{left:0;top:720px;width:1056px;height:206px;background:var(--grey-bg);border-top:1px solid #e2e2e2}
.sec-title{font-size:12.5px;font-weight:600;color:var(--blue);display:flex;align-items:center;gap:10px}
.sec-title::after{content:"";flex:1;height:1px;background:#d8d8d8}
.about-img{left:190px;top:769px;width:165px;height:109px;background:linear-gradient(135deg,#e6e8ea,#c8ccd0)}
.about-text{left:366px;top:769px;width:260px;font-size:8.8px;line-height:12.8px;color:#666}
.btn{left:538px;top:867px;width:86px;height:23px;background:var(--blue);color:var(--white);font-size:10px;line-height:23px;padding-left:10px}
.btn i{position:absolute;right:9px;top:6px;width:11px;height:11px;border:1px solid var(--white)}
.btn i::before,.btn i::after{content:"";position:absolute;background:var(--white);left:2px;top:4px;width:5px;height:1px}
.btn i::after{transform:rotate(90deg)}
.arrows{display:flex;gap:3px}
.arrows span{width:14px;height:14px;display:flex;align-items:center;justify-content:center}
.quote{left:658px;top:774px;width:208px;font-size:9.3px;font-style:italic;color:#777;line-height:14px;padding-left:20px}
.quote::before{content:"\201C";position:absolute;left:0;top:-6px;font-size:24px;color:var(--teal);font-style:normal;font-weight:700}
.author{right:238px;top:858px;text-align:left;font-size:10px;color:var(--teal)}
.author small{display:block;font-size:8px;color:#555;line-height:9px}
.avatar{left:824px;top:849px;width:42px;height:42px;border-radius:50%;border:2px solid var(--teal);background:linear-gradient(#d8dde0,#9aa3aa)}
/* footer */
.foot{left:0;top:926px;width:1056px;height:211px;background:var(--teal)}
.ftitle{font-size:11.5px;font-weight:600;color:var(--white);display:flex;align-items:center;gap:10px}
.ftitle::after{content:"";flex:1;height:1px;background:rgba(255,255,255,.35)}
.news{font-size:8.6px;line-height:11px;color:var(--white);padding-bottom:8px;margin-bottom:8px;border-bottom:1px solid rgba(255,255,255,.35)}
.news span,.post span{color:var(--teal-light)}
.news:last-child{border:0}
.post{display:flex;gap:8px;font-size:8.6px;line-height:11px;color:var(--white);padding-bottom:14px;margin-bottom:14px;border-bottom:1px solid rgba(255,255,255,.35)}
.post:last-child{border:0}
.thumb{width:50px;height:50px;flex:none;background:linear-gradient(135deg,#e8eaec,#8d969d)}
.form label{position:absolute;left:0;font-size:8.8px;color:var(--white)}
.form label::after{content:":";position:absolute;left:47px}
.form .field{position:absolute;left:53px;width:96px;background:var(--teal-deep)}
.submit{left:612px;top:1087px;width:66px;height:22px;background:var(--teal-deep);color:var(--white);font-size:9.5px;text-align:center;line-height:22px}
.wait{left:697px;top:940px;width:169px;height:168px;background:var(--teal-deep)}
.wait .inner{position:absolute;left:9px;top:9px;right:9px;bottom:9px;border:1px dashed rgba(255,255,255,.5);padding:6px 9px;color:var(--white)}
.wait h4{font-size:11.5px;font-weight:600}
.num{display:flex;align-items:center;gap:4px;margin:9px 0 12px;font-size:11.5px}
.num b{width:28px;height:28px;background:var(--teal);font-size:22px;font-weight:400;text-align:center;line-height:28px}
.wait p{font-size:8.6px;line-height:11px}
.bottom{left:0;top:1137px;width:1056px;height:63px;background:var(--blue);font-size:8.8px;color:var(--teal-light)}
</style>
</head>
<body>
<div class="abs topbar"></div>
<div class="abs social"><span></span><span></span><span></span></div>
<div class="abs call">Call Now : (555) 014-2290</div>

<div class="abs brand"><i></i><b>CREST MEDICAL CENTER</b></div>
<nav class="abs nav">
  <a>WHY CREST</a><a>PHYSICIAN</a><a>SPECIALITES</a><a>INFO</a>
  <a class="active">LOCATION<small>Where we are</small></a>
  <a class="last">CONTAT US</a>
</nav>

<section class="abs hero" role="img" aria-label="Photograph of a senior doctor with a clipboard speaking with a patient"></section>
<div class="abs dropdown"><div>LOCATION -1</div><div class="hover">LOCATION-2</div><div>LOCATION-3</div></div>
<h1 class="abs headline">PHYSICIAN OWNED. PATIENT-FOCUSED</h1>
<p class="abs subline">Lorem Ipsum is simply dummy text of the printing and typesetting industry. Lorem Ipsum has been the industry's standard dummy text..</p>
<div class="abs dots"><span></span><span></span><span></span><span></span><span></span></div>

<div class="abs diamond" style="left:401px;background:var(--teal)"><svg viewBox="0 0 59 59" fill="none" stroke="#fff" stroke-width="2"><path d="M22 19v9a7 7 0 0 0 14 0v-9"/><path d="M29 35v4a5 5 0 0 0 10 0v-9"/><circle cx="39" cy="27" r="2.5"/></svg></div>
<div class="abs diamond" style="left:499px;background:var(--blue)"><svg viewBox="0 0 59 59" fill="none" stroke="#fff" stroke-width="1.8"><rect x="18" y="19" width="23" height="21"/><path d="M22 25h15M22 29h15M22 33h15M22 37h10"/></svg></div>
<div class="abs diamond" style="left:597px;background:var(--blue)"><svg viewBox="0 0 59 59"><text x="29.5" y="40" text-anchor="middle" font-family="Open Sans,sans-serif" font-size="28" font-weight="700" fill="#45adb9">?</text></svg></div>

<div class="abs feat-img" role="img" aria-label="Photograph of a surgical team in scrubs"><p>WHAT SETS US<br><b>APART</b></p></div>
<div class="abs feat teal" style="left:389px;width:149px"><h3>TECHNOLOGY</h3>Lorem Ipsum is simply dummy text of the printing and typesetting industry. Lorem Ipsum has been the industry's</div>
<div class="abs feat blue" style="left:553px;width:149px"><h3>QUALITY OF CORE</h3>Lorem Ipsum is simply dummy text of the printing and typesetting industry. Lorem Ipsum has been the industry's</div>
<div class="abs feat blue" style="left:716px;width:150px"><h3>TECHNOLOGY</h3>Lorem Ipsum is simply dummy text of the printing and typesetting industry. Lorem Ipsum has been the industry's</div>

<section class="abs band"></section>
<h2 class="abs sec-title" style="left:190px;top:746px;width:458px">CREST MEDICAL CENTER</h2>
<div class="abs about-img" role="img" aria-label="Photograph of a doctor examining a patient in a clinic room"></div>
<p class="abs about-text">Lorem Ipsum is simply dummy text of the printing and typesetting industry. Lorem Ipsum has been the industry's standard dummy text ever since the 1500s, when an unknown printer took a galley of type and scrambled it to make a type specimen book. It has survived not only five centuries, but also the leap into electronic typesetting, remaining essentially unchanged. It was popularised in the 1960s.</p>
<div class="abs btn">Read More<i></i></div>

<h2 class="abs sec-title" style="left:658px;top:746px;width:170px">TESTIMONIALS</h2>
<div class="abs arrows" style="left:833px;top:748px">
  <span style="background:var(--blue)"><svg width="6" height="8"><path d="M5 0L1 4l4 4" stroke="#fff" fill="none"/></svg></span>
  <span style="background:var(--teal)"><svg width="6" height="8"><path d="M1 0l4 4-4 4" stroke="#fff" fill="none"/></svg></span>
</div>
<p class="abs quote">Lorem Ipsum is simply dummy text look of the printing and typesetting industry. simpl Lorem Ipsum has been the industry's standard&nbsp; of the dummy text ever since the when Ipsum</p>
<div class="abs author" style="left:757px;right:auto">Dana Whitfield<small>Police officer</small></div>
<div class="abs avatar" role="img" aria-label="Portrait photo of the reviewer"></div>

<footer class="abs foot"></footer>
<h3 class="abs ftitle" style="left:189px;top:955px;width:112px">NEWS</h3>
<div class="abs arrows" style="left:305px;top:957px">
  <span style="border:1px solid #fff"><svg width="6" height="8"><path d="M5 0L1 4l4 4" stroke="#fff" fill="none"/></svg></span>
  <span style="border:1px solid #fff"><svg width="6" height="8"><path d="M1 0l4 4-4 4" stroke="#fff" fill="none"/></svg></span>
</div>
<div class="abs" style="left:190px;top:980px;width:146px">
  <div class="news"><span>22-7-2013: Lorem Ipsum is dummy text :</span> of the printing and typesetting industry. has been</div>
  <div class="news"><span>22-7-2013: Lorem Ipsum is simdummy text :</span> of the printing and typesetting industry.</div>
  <div class="news"><span>22-7-2013: Lorem Ipsum</span> is simply dummy text : of the</div>
</div>
<h3 class="abs ftitle" style="left:353px;top:955px;width:157px">BLOG</h3>
<div class="abs" style="left:354px;top:981px;width:152px">
  <div class="post"><div class="thumb" role="img" aria-label="Photo of a businessman at a desk"></div><p><span>Lorem Ipsum is simply dummy text</span> of the printing and typesetting industry.</p></div>
  <div class="post"><div class="thumb" role="img" aria-label="Photo of a businessman at a desk"></div><p><span>Lorem Ipsum is simply dummy text</span> of the printing and typesetting industry.</p></div>
</div>
<h3 class="abs ftitle" style="left:529px;top:955px;width:149px">QUICK CONTACT</h3>
<div class="abs form" style="left:529px;top:983px;width:149px;height:100px">
  <label style="top:2px">Name</label><div class="field" style="top:0;height:15px"></div>
  <label style="top:23px">Email</label><div class="field" style="top:21px;height:15px"></div>
  <label style="top:44px">Comment</label><div class="field" style="top:42px;height:56px"></div>
</div>
<div class="abs submit">SUBMIT</div>
<div class="abs wait"><div class="inner">
  <h4>AVRAGE WAIT TIME</h4>
  <div class="num"><b>9</b>MINITES</div>
  <p>printing and typesetting industry. has been the industry's standard dummy text ever since the</p>
</div></div>

<div class="abs bottom">
  <span class="abs" style="left:190px;top:19px">Copyright © 2013 Allright Reserved</span>
  <span class="abs" style="right:190px;top:19px">Sitemap &nbsp;|&nbsp; Privecy policy</span>
</div>
</body>
</html>
```